Stationery Design Project

Hi, we have a group of companies which operate within different industries, we have decided on a parent company logo and name and now require stationary and business cards to use for the staff who work across all three companies.

I would expect the designs to show the new parent company logo prominently, and if possible still have the three individual company logos shown. I have attached all of the logos and current letterheads and business cards for a example of what we have gone with in the past. Please note outside the box thinking is appreciated.

Any questions please let me know.

Industry/Entity Type

Business

Requirements
Must have
• Must show all 4 logos.

Designs for business card and letterhead.

```html
<!DOCTYPE html>
<html lang="en">
<head>
<meta charset="utf-8">
<title>Harbourline Group Stationery</title>
<link href="https://fonts.googleapis.com/css2?family=Jost:wght@400;500;600;700&display=swap" rel="stylesheet">
<style>
  :root {
    --backdrop: #352b63;
    --paper: #ffffff;
    --navy: #33297a;
    --green: #7dbb3f;
    --label-blue: #1e3d8f;
    --text-grey: #7f7f7f;
    --mark-grey: #9a9a9a;
  }
  * { margin: 0; padding: 0; box-sizing: border-box; }
  html, body { width: 1200px; height: 900px; overflow: hidden; }
  body {
    background: var(--backdrop);
    font-family: "Jost", "Futura", sans-serif;
    position: relative;
  }
  .letterhead {
    position: absolute; left: 230px; top: 39px;
    width: 638px; height: 823px;
    background: var(--paper);
    box-shadow: 4px 4px 8px rgba(0,0,0,.35);
    color: var(--text-grey);
  }
  .brand {
    position: absolute; display: flex; align-items: center; gap: 6px;
    color: var(--navy); font-weight: 700; letter-spacing: .5px;
    white-space: nowrap;
  }
  .brand-dot { width: 8px; height: 8px; border-radius: 50%; background: var(--green); flex: none; }
  .letterhead .brand { left: 38px; top: 54px; font-size: 24px; line-height: 30px; }
  .contact-line {
    font-size: 8px; letter-spacing: .8px; text-transform: uppercase; color: #555;
    white-space: nowrap;
  }
  .contact-line .label { color: var(--label-blue); font-weight: 600; }
  .letterhead .contacts { position: absolute; right: 38px; top: 54px; text-align: right; line-height: 14px; }
  .letter { position: absolute; left: 94px; width: 450px; font-size: 10px; line-height: 12.2px; }
  .letter.date { top: 126px; }
  .letter.recipient { top: 170px; }
  .letter.salutation { top: 228px; }
  .letter.p1 { top: 254px; }
  .letter.p2 { top: 361px; }
  .letter.p3 { top: 431px; }
  .letter.p4 { top: 486px; }
  .letter.closing { top: 528px; }
  .letter.signature { top: 594px; }
  .company-row {
    position: absolute; left: 58px; right: 58px; top: 722px;
    display: flex; justify-content: space-between; align-items: center;
  }
  .company-name { font-size: 17px; font-weight: 700; color: var(--mark-grey); letter-spacing: .5px; text-transform: uppercase; white-space: nowrap; }
  .card { position: absolute; left: 831px; width: 263px; height: 150px; box-shadow: 4px 4px 8px rgba(0,0,0,.35); }
  .card-front { top: 169px; background: var(--paper); }
  .card-front .brand { left: 14px; top: 12px; font-size: 14px; gap: 5px; }
  .card-front .brand-dot { width: 5px; height: 5px; }
  .card-person { position: absolute; left: 0; right: 0; top: 61px; padding-left: 60px; text-align: center; white-space: nowrap; }
  .card-person .name { color: var(--label-blue); font-size: 11.5px; font-weight: 500; }
  .card-person .role { color: #666; font-size: 6.5px; letter-spacing: .8px; }
  .card-front .contacts { position: absolute; right: 14px; top: 113px; text-align: right; line-height: 12px; }
  .card-front .contact-line { font-size: 6.4px; letter-spacing: .3px; }
  .card-back {
    top: 361px; background: var(--green);
    display: grid; grid-template-columns: repeat(3, 1fr); column-gap: 12px;
    align-items: center; padding: 0 14px;
  }
  .card-back .company-name {
    color: var(--paper); font-size: 10px; line-height: 13px;
    white-space: normal; text-align: center;
  }
</style>
</head>
<body>
  <section class="letterhead">
    <div class="brand"><span>HARBOURLINE</span><span class="brand-dot"></span></div>
    <div class="contacts">
      <p class="contact-line">22 Quartz Road &nbsp; PO Box 318 &nbsp; Redbank QLD 4301 &nbsp; Australia</p>
      <p class="contact-line"><span class="label">Web</span> harbourline.au.com &nbsp; <span class="label">Phone</span> 07 3900 1200 &nbsp; <span class="label">Fax</span> 07 3900 1300</p>
    </div>
    <p class="letter date">Month 15, 2012</p>
    <p class="letter recipient">Mr. Jim Smith<br>000 Anystreet Avenue<br>Anywhere, OR 97302</p>
    <p class="letter salutation">Dear Harbourline,</p>
    <p class="letter p1">Lorem ipsum dolor sit amet, consectetuer adipiscing elit, sed diam nonummy nibh euismod tincidunt ut laoreet dolore magna aliquam erat volutpat. Ut wisi enim ad minim veniam, quis nostrud exerci tation ullamcorper suscipit lobortis nisl ut aliquip ex ea commodo consequat. Duis autem vel eum iriure dolor in hendrerit in vulputate velit esse molestie consequat, vel illum dolore eu feugiat nulla facilisis at vero eros et accumsan et iusto odio dignissim qui blandit praesent luptatum zzril delenit augue duis dolore te feugait nulla facilisi. Lorem ipsum dolor sit amet, consectetuer adipiscing elit, sed diam nonummy nibh euismod tincidunt ut laoreet dolore magna aliquam erat volutpat.</p>
    <p class="letter p2">Ut wisi enim ad minim veniam, quis nostrud exerci tation ullamcorper suscipit lobortis nisl ut aliquip ex ea commodo consequat. Duis autem vel eum iriure dolor in hendrerit in vulputate velit esse molestie consequat, vel illum dolore eu feugiat nulla facilisis at vero eros et accumsan et iusto odio dignissim qui blandit praesent luptatum zzril delenit augue duis dolore te feugait nulla facilisi.</p>
    <p class="letter p3">Nam liber tempor cum soluta nobis eleifend option congue nihil imperdiet doming id quod mazim placerat facer possim assum. Lorem ipsum dolor sit amet, consectetuer adipiscing elit, sed diam nonummy nibh euismod tincidunt ut laoreet dolore.</p>
    <p class="letter p4">Lorem ipsum dolor sit amet, consectetuer adipiscing elit, sed diam nonummy nibh euismod tincidunt.</p>
    <p class="letter closing">Sincerely,</p>
    <p class="letter signature">John Q. Person<br>Executive Director<br>jperson@harbourline.au.com</p>
    <div class="company-row">
      <span class="company-name">Harbourline Patios</span>
      <span class="company-name">Formwell</span>
      <span class="company-name">Crease Metalworks</span>
    </div>
  </section>

  <section class="card card-front">
    <div class="brand"><span>HARBOURLINE</span><span class="brand-dot"></span></div>
    <div class="card-person">
      <p class="name">John Q. Person</p>
      <p class="role">PRESIDENT</p>
    </div>
    <div class="contacts">
      <p class="contact-line">22 Quartz Road &nbsp; PO Box 318 &nbsp; Redbank QLD 4301 &nbsp; Australia</p>
      <p class="contact-line"><span class="label">Web</span> harbourline.au.com &nbsp; <span class="label">Phone</span> 07 3900 1200 &nbsp; <span class="label">Fax</span> 07 3900 1300</p>
    </div>
  </section>

  <section class="card card-back">
    <span class="company-name">Harbourline Patios</span>
    <span class="company-name">Formwell</span>
    <span class="company-name">Crease Metal</span>
  </section>
</body>
</html>
```